Modern card design needed for building development company

We are looking for a sharp modern new look for our business cards.
We are a New Zealand based company called TKV Ventures NZ LTD that specialises in subdividing large sections, housing and commercial buildings.
We have attached a photo of the current logo and would like to see it improved somehow as it looks a bit dated.
We are open to any colours.

Target Market(s)

Investors, Property buyers

Industry/Entity Type

Investment

Contact Information for Business Card

TKV VENTURES NZ LTD
www.tkvventuresnz.co.nz

Howard Pennick
Phone +64 21 843 192
Email hdpennick@fernmail.co.nz

Font styles to use
Serif
Sans Serif

Colors
0792cd
33a6d7
85cae6
6b449b
886aae
f04a50
ec1f27
f37122
f68d4d

Requirements
Must have
• Please try and make the logo more modern or if you have a similar one we would like to see it.

```html
<!DOCTYPE html>
<html lang="en">
<head>
<meta charset="UTF-8">
<title>TKV Ventures NZ LTD — Business Card</title>
<link href="https://fonts.googleapis.com/css2?family=Work+Sans:wght@400;600&display=swap" rel="stylesheet">
<style>
  :root {
    --backdrop: #2b2b2b;
    --card: #ffffff;
    --brand: #9c1a2f;
    --ink: #3d3d3d;
    --on-brand: #ffffff;
  }
  * { margin: 0; padding: 0; box-sizing: border-box; }
  html, body {
    width: 1200px; height: 900px; overflow: hidden;
    background: var(--backdrop);
    font-family: "Work Sans", Arial, sans-serif;
  }
  .canvas {
    position: relative; width: 1200px; height: 900px;
  }
  .card {
    position: absolute; left: 267px;
    width: 666px; height: 380px;
    background: var(--card);
    border-radius: 16px;
    overflow: hidden;
  }
  .card--front { top: 50px; }
  .card--back { top: 470px; }

  .wordmark {
    display: flex; align-items: center; gap: 10px;
    color: var(--brand); font-weight: 600;
  }
  .wordmark__square {
    width: 14px; height: 14px; background: var(--brand); flex: none;
  }
  .wordmark__text { line-height: 1.15; letter-spacing: 0.04em; }
  .wordmark__sub { display: block; font-size: 0.5em; letter-spacing: 0.3em; text-align: center; }

  .card--front .wordmark {
    position: absolute; left: 50%; top: 50%;
    transform: translate(-50%, -50%);
    font-size: 26px;
  }

  .card--back .wordmark {
    position: absolute; left: 56px; top: 162px;
    font-size: 21px;
  }
  .divider {
    position: absolute; left: 312px; top: 110px;
    width: 2px; height: 148px; background: var(--brand);
  }
  .contact {
    position: absolute; left: 348px; top: 150px;
  }
  .contact__name {
    color: var(--brand); font-weight: 600; font-size: 27px;
    letter-spacing: 0.01em; margin-bottom: 10px;
  }
  .contact__line {
    display: flex; align-items: center; gap: 10px;
    color: var(--ink); font-size: 17px; line-height: 1.45;
  }
  .contact__line svg { width: 12px; height: 12px; flex: none; }

  .web-band {
    position: absolute; right: 0; bottom: 0;
    width: 420px; height: 52px;
    background: var(--brand);
    clip-path: polygon(50px 0, 100% 0, 100% 100%, 0 100%);
    color: var(--on-brand);
    display: flex; align-items: center; justify-content: flex-end;
    padding-right: 26px;
    font-size: 17px; letter-spacing: 0.02em;
  }
</style>
</head>
<body>
<main class="canvas">
  <section class="card card--front">
    <div class="wordmark">
      <span class="wordmark__square"></span>
      <span class="wordmark__text">TKV VENTURES<span class="wordmark__sub">NZ LTD</span></span>
    </div>
  </section>

  <section class="card card--back">
    <div class="wordmark">
      <span class="wordmark__square"></span>
      <span class="wordmark__text">TKV VENTURES<span class="wordmark__sub">NZ LTD</span></span>
    </div>
    <div class="divider"></div>
    <div class="contact">
      <h1 class="contact__name">HOWARD PENNICK</h1>
      <p class="contact__line">
        <svg viewBox="0 0 12 12" aria-hidden="true"><path d="M3 1 L5 3.5 L4 5 Q5 7 7 8 L8.5 7 L11 9 L9.5 11 Q5 10.5 1 3 Z" fill="none" stroke="var(--brand)" stroke-width="1.2"/></svg>
        +64 21 843 192
      </p>
      <p class="contact__line">
        <svg viewBox="0 0 12 12" aria-hidden="true"><rect x="1" y="2.5" width="10" height="7" fill="none" stroke="var(--brand)" stroke-width="1.2"/><path d="M1 2.5 L6 6.5 L11 2.5" fill="none" stroke="var(--brand)" stroke-width="1.2"/></svg>
        hdpennick@fernmail.co.nz
      </p>
    </div>
    <div class="web-band">www.tkvventuresnz.co.nz.com</div>
  </section>
</main>
</body>
</html>
```